New Business Cards for Organic Meat Farm

We need a business card designed for Thornbury Farm, a meat farm in western MA. Our logo uses a hand-drawn woodcut (attached). Our color palette has been simply black and white (shown in notepad and picture of our food truck). While we are based out of western MA, we have ambitions to grow nationally, so our hope is for a classy and memorable card which will be printed on a premium quality stock from a printer like printkestrel.com.
Target Market(s)
consumers of quality meats, restauranteurs, partnering farms
Industry/Entity Type
Farming and prepared meat products
Contact Information for Business Card
Wendell Pruitt, President/Owner, wendell@thornburyfarm.com, mobile: 413-555-0172, phone: 413-555-0148, thornburyfarm.com, facebook: @thornburyfarm, instagram: @thornburyfarmma
Colors
Designer to choose colors to be used in the design.
Look and feel

```html
<!DOCTYPE html>
<html lang="en">
<head>
<meta charset="utf-8">
<title>Thornbury Farm – Business Card</title>
<link rel="stylesheet" href="https://fonts.googleapis.com/css2?family=Jost:wght@400;500&family=Lobster&display=swap">
<style>
  :root {
    --backdrop: #8f8f8f;
    --charcoal: #3a3a3c;
    --charcoal-light: #48484b;
    --ink: #333335;
    --paper: #ffffff;
    --muted-ink: #4a4a4c;
  }
  * { margin: 0; padding: 0; box-sizing: border-box; }
  html, body {
    width: 1200px; height: 1000px; overflow: hidden;
    background: var(--backdrop);
    font-family: "Jost", "Helvetica Neue", Arial, sans-serif;
  }
  .canvas { position: relative; width: 1200px; height: 1000px; }

  .card {
    position: absolute; left: 253px; width: 694px; height: 399px;
    border-radius: 18px; overflow: hidden;
  }
  .card--front { top: 68px; background: var(--charcoal); color: var(--paper); }
  .card--back { top: 525px; background: var(--paper); color: var(--ink); }

  /* front */
  .front-artwork {
    position: absolute; inset: 0;
    background: radial-gradient(ellipse at 55% 50%, var(--charcoal-light) 0%, var(--charcoal) 75%);
  }
  .front-brand {
    position: absolute; left: 0; right: 0; top: 170px; text-align: center;
  }
  .brand-name {
    font-family: "Jost", "Helvetica Neue", Arial, sans-serif;
    font-weight: 500; text-transform: uppercase; letter-spacing: 0.14em;
    line-height: 1.15;
  }
  .front-brand .brand-name { font-size: 40px; color: var(--paper); }
  .front-url {
    position: absolute; left: 0; right: 0; top: 351px; text-align: center;
    font-size: 17px; letter-spacing: 0.32em; font-weight: 500;
  }

  /* back */
  .back-logo { position: absolute; left: 57px; top: 93px; width: 236px; text-align: center; }
  .back-artwork {
    width: 236px; height: 105px; border-radius: 4px;
    background: linear-gradient(180deg, #e6e6e6 0%, #bdbdbd 100%);
  }
  .back-logo .brand-name { font-size: 31px; color: var(--ink); margin-top: 14px; }

  .contact { position: absolute; left: 330px; width: 296px; top: 95px; text-align: center; }
  .contact-name { font-family: "Lobster", "Brush Script MT", cursive; font-size: 46px; line-height: 1.1; color: var(--ink); }
  .contact-title { margin-top: 10px; font-size: 16px; letter-spacing: 0.14em; color: var(--muted-ink); font-weight: 500; }
  .contact-icons { margin-top: 10px; display: flex; justify-content: center; gap: 6px; }
  .contact-icons svg { width: 25px; height: 25px; }
  .contact-lines { margin-top: 6px; font-size: 16.5px; line-height: 22px; letter-spacing: 0.06em; color: var(--ink); }

  .social {
    position: absolute; left: 0; right: 0; top: 356px; text-align: center;
    font-size: 14.5px; letter-spacing: 0.06em; color: var(--ink);
  }
  .social-dot {
    display: inline-block; width: 14px; height: 14px; border-radius: 50%;
    background: var(--ink); vertical-align: -2px; margin-right: 4px;
  }
</style>
</head>
<body>
<main class="canvas">
  <section class="card card--front" aria-label="Card front">
    <div class="front-artwork" role="img" aria-label="Faint woodcut illustration of the farmhouse with trees filling the card"></div>
    <div class="front-brand">
      <div class="brand-name">Thornbury Farm</div>
    </div>
    <div class="front-url">THORNBURYFARM.COM</div>
  </section>

  <section class="card card--back" aria-label="Card back">
    <div class="back-logo">
      <div class="back-artwork" role="img" aria-label="Woodcut illustration of the farmhouse among trees"></div>
      <div class="brand-name">Thornbury Farm</div>
    </div>

    <div class="contact">
      <div class="contact-name">Wendell Pruitt</div>
      <div class="contact-title">PRESIDENT/OWNER</div>
      <div class="contact-icons">
        <svg viewBox="0 0 26 26" aria-label="Email"><circle cx="13" cy="13" r="13" fill="#333335"/><rect x="6.5" y="8.5" width="13" height="9" fill="none" stroke="#fff" stroke-width="1.4"/><path d="M6.5 8.5 13 14l6.5-5.5" fill="none" stroke="#fff" stroke-width="1.4"/></svg>
        <svg viewBox="0 0 26 26" aria-label="Mobile"><circle cx="13" cy="13" r="13" fill="#333335"/><rect x="9.5" y="5.5" width="7" height="15" rx="1.5" fill="none" stroke="#fff" stroke-width="1.4"/><circle cx="13" cy="18" r="0.9" fill="#fff"/></svg>
        <svg viewBox="0 0 26 26" aria-label="Phone"><circle cx="13" cy="13" r="13" fill="#333335"/><path d="M9 6.5l2.3 3-1.4 1.6c.9 2 2.3 3.4 4.2 4.3l1.6-1.4 3 2.3-1.4 2.3c-5 0-9.8-4.8-9.8-9.8z" fill="#fff"/></svg>
      </div>
      <div class="contact-lines">
        <div>wendell@thornburyfarm.com</div>
        <div>413-555-0172</div>
        <div>413-555-0148</div>
      </div>
    </div>

    <div class="social"><span class="social-dot"></span>@thornburyfarm • <span class="social-dot"></span>@thornburyfarmma</div>
  </section>
</main>
</body>
</html>
```